LedgaVue Business Card

We need a business card design using the attached logo. The company is a financial services company that provides a dashboard (chart based information) for Executives of small businesses to use to better manage their information. The design must be progressive, make good utilization of the logo and project stability and financial security.

Industry/Entity Type

Financial

```html
<!DOCTYPE html>
<html lang="en">
<head>
<meta charset="utf-8">
<title>LedgaVue Business Card</title>
<link href="https://fonts.googleapis.com/css2?family=Open+Sans:wght@400;600;700&display=swap" rel="stylesheet">
<style>
  :root {
    --brand-red: #a31e22;
    --ink: #1b1b1b;
    --text-grey: #3a3a3a;
    --paper: #ffffff;
    --backdrop: #e8e5e2;
    --faint-mark: #f1eeee;
  }
  * { box-sizing: border-box; margin: 0; padding: 0; }
  html, body {
    width: 1200px;
    height: 471px;
    overflow: hidden;
  }
  body {
    background: var(--backdrop);
    font-family: "Open Sans", Arial, sans-serif;
    position: relative;
  }
  .card {
    position: absolute;
    top: 80px;
    width: 540px;
    height: 310px;
    box-shadow: 0 4px 14px rgba(0,0,0,0.18);
    overflow: hidden;
  }
  .card--front { left: 40px; background: var(--paper); }
  .card--back { left: 620px; background: var(--brand-red); }

  .front-mark {
    position: absolute;
    left: 40px;
    top: 40px;
    width: 230px;
    height: 230px;
    background: var(--faint-mark);
    border-radius: 10px;
  }
  .brand {
    position: absolute;
    display: flex;
    align-items: center;
    gap: 12px;
    font-weight: 700;
    letter-spacing: -0.5px;
  }
  .brand__square {
    display: block;
    background: var(--brand-red);
    border-radius: 4px;
  }
  .card--front .brand {
    left: 210px;
    top: 28px;
    font-size: 44px;
    color: var(--ink);
  }
  .card--front .brand__square { width: 40px; height: 40px; }

  .person {
    position: absolute;
    left: 340px;
    top: 122px;
  }
  .person__name {
    color: var(--brand-red);
    font-size: 19px;
    font-weight: 600;
    line-height: 1.1;
  }
  .person__role {
    color: var(--ink);
    font-size: 13px;
    line-height: 1.4;
  }
  .contact {
    position: absolute;
    left: 350px;
    top: 190px;
    list-style: none;
    color: var(--text-grey);
    font-size: 13px;
    line-height: 20px;
  }
  .contact li { display: flex; align-items: center; gap: 4px; }
  .contact svg { width: 11px; height: 11px; fill: none; stroke: var(--text-grey); stroke-width: 1.6; }
  .address {
    position: absolute;
    left: 362px;
    top: 262px;
    color: var(--text-grey);
    font-size: 13px;
    line-height: 17px;
    font-style: normal;
  }

  .card--back .brand {
    left: 50%;
    top: 50%;
    transform: translate(-50%, -50%);
    font-size: 62px;
    color: var(--paper);
    gap: 16px;
  }
  .card--back .brand__square {
    width: 70px;
    height: 70px;
    background: var(--paper);
    border-radius: 6px;
  }
</style>
</head>
<body>
  <section class="card card--front" aria-label="Business card front">
    <div class="front-mark" aria-hidden="true"></div>
    <div class="brand"><span class="brand__square"></span><span class="brand__name">LedgaVue</span></div>
    <div class="person">
      <p class="person__name">Your Name</p>
      <p class="person__role">Designation</p>
    </div>
    <ul class="contact">
      <li>
        <svg viewBox="0 0 12 12" aria-hidden="true"><circle cx="6" cy="6" r="5"/><path d="M4 3.5 L5 5 L4.5 6 Q5.5 7.5 6.5 8 L7.5 7.5 L9 8.5"/></svg>
        123-456-7890
      </li>
      <li>
        <svg viewBox="0 0 12 12" aria-hidden="true"><rect x="1" y="3" width="10" height="7"/><path d="M1 3 L6 7 L11 3"/></svg>
        hello@ledgavue.com
      </li>
      <li>
        <svg viewBox="0 0 12 12" aria-hidden="true"><circle cx="6" cy="6" r="5"/><ellipse cx="6" cy="6" rx="2.2" ry="5"/><path d="M1 6 H11"/></svg>
        www.ledgavue.com
      </li>
    </ul>
    <address class="address">Street Name City Name<br>State Zipcode</address>
  </section>

  <section class="card card--back" aria-label="Business card back">
    <div class="brand"><span class="brand__square"></span><span class="brand__name">LedgaVue</span></div>
  </section>
</body>
</html>
```